Harrowfield Nature Alliance needs a poster for fish fry

We need a flyer made for a fish fry. Things we need on it;

Date: Sunday, February 12th
Location: Brenmoor Sportsdome Auditorium
Time: 5-6:30 pm
Cost: $15 for adults, $10 for 12 & under, free for preschool

Requirements
Must have
• Must have our logo on it.

```html
<!DOCTYPE html>
<html lang="en">
<head>
<meta charset="utf-8">
<title>Harrowfield Nature Alliance – Fish Fry Flyer</title>
<link rel="stylesheet" href="https://fonts.googleapis.com/css2?family=Kaushan+Script&family=Anton&family=Montserrat:wght@500;700;800;900&display=swap">
<style>
  :root {
    --page: #ececec;
    --ink: #1a1a1a;
    --ink-soft: #262626;
    --paper: #ffffff;
    --orange: #f7a823;
    --white: #ffffff;
    --muted: #5c5c5c;
    --stamp: #3c8fa3;
    --fish-a: #a0632d;
    --fish-b: #4d2c17;
    --plate-a: #b76a34;
    --plate-b: #3e5a2a;
  }
  * { box-sizing: border-box; margin: 0; padding: 0; }
  html, body { width: 1200px; height: 2196px; overflow: hidden; }
  body { background: var(--page); font-family: "Montserrat", sans-serif; position: relative; }

  .flyer {
    position: absolute; left: 100px; top: 393px;
    width: 1000px; height: 1410px;
    background: var(--paper); overflow: hidden;
  }
  .flyer-dark { position: absolute; left: 0; top: 0; width: 1000px; height: 1110px; }

  .brand { position: absolute; left: 70px; top: 120px; display: flex; align-items: center; gap: 16px; }
  .brand-dot { width: 44px; height: 44px; border-radius: 50%; background: var(--white); }
  .brand-name { color: var(--white); font-weight: 800; font-size: 26px; line-height: 1.15; text-transform: uppercase; letter-spacing: 1px; width: 260px; }

  .date-badge {
    position: absolute; left: 560px; top: 68px; width: 200px; height: 200px;
    border-radius: 50%; border: 3px dashed var(--white);
    display: flex; flex-direction: column; align-items: center; justify-content: center;
    text-align: center; font-weight: 800; color: var(--white);
  }
  .date-day-num { color: var(--orange); font-size: 54px; line-height: 1; }
  .date-month { font-size: 28px; line-height: 1.2; }
  .date-weekday { font-size: 24px; line-height: 1.1; }

  .photo { position: absolute; }
  .photo-fish-board { left: 600px; top: 240px; width: 480px; height: 520px; border-radius: 40px; transform: rotate(-14deg);
    background: radial-gradient(circle at 40% 45%, var(--fish-a), var(--fish-b) 75%); }
  .photo-plate { left: 20px; top: 880px; width: 400px; height: 380px; border-radius: 50%;
    background: radial-gradient(circle at 50% 50%, var(--plate-a) 0 45%, var(--plate-b) 70%, #e9e9e9 72%); }

  .title { position: absolute; left: 85px; top: 380px; }
  .title-fish { font-family: "Kaushan Script", cursive; color: var(--white); font-size: 150px; line-height: 1; }
  .title-fry { font-family: "Anton", sans-serif; color: var(--orange); font-size: 200px; line-height: 0.9; letter-spacing: 4px; }

  .prices { position: absolute; left: 90px; top: 730px; display: flex; flex-direction: column; gap: 24px; }
  .price-row { display: flex; align-items: center; width: 360px; justify-content: space-between; }
  .price-label { color: var(--white); font-weight: 800; font-size: 26px; }
  .price-value { background: var(--orange); color: var(--ink); font-weight: 900; font-size: 38px; width: 110px; text-align: center; padding: 4px 0; }

  .free-badge { position: absolute; left: 520px; top: 740px; width: 270px; height: 140px; transform: rotate(-4deg); }
  .free-badge svg { position: absolute; inset: 0; }
  .free-text { position: absolute; inset: 0; display: flex; flex-direction: column; align-items: center; justify-content: center; color: var(--ink); }
  .free-word { font-family: "Anton", sans-serif; font-size: 66px; line-height: 1; }
  .free-sub { font-weight: 800; font-size: 19px; letter-spacing: 1px; }

  .details { position: absolute; left: 500px; top: 1130px; }
  .detail-label { display: inline-block; background: var(--orange); color: var(--ink); font-weight: 800; font-size: 20px; padding: 3px 10px; margin-bottom: 8px; }
  .detail-value { color: var(--muted); font-weight: 700; font-size: 20px; margin-bottom: 22px; width: 260px; line-height: 1.3; }

  .stamp { position: absolute; left: 790px; top: 1110px; width: 190px; height: 190px; border-radius: 50%;
    border: 4px solid var(--stamp); display: flex; align-items: center; justify-content: center; transform: rotate(-8deg); }
  .stamp-inner { width: 156px; height: 156px; border-radius: 50%; border: 2px solid var(--stamp);
    display: flex; align-items: center; justify-content: center; text-align: center;
    font-family: "Anton", sans-serif; color: var(--stamp); font-size: 40px; line-height: 1; }
</style>
</head>
<body>
  <main class="flyer">
    <svg class="flyer-dark" viewBox="0 0 1000 1110" aria-hidden="true">
      <path fill="var(--ink)" d="M0 0H1000V1060L960 1072 930 1058 880 1080 840 1064 790 1086 740 1066 690 1090 640 1070 590 1094 540 1074 500 1098 450 1078 400 1096 340 1074 290 1092 230 1070 170 1090 110 1068 60 1086 0 1066Z"/>
    </svg>

    <div class="brand">
      <span class="brand-dot"></span>
      <span class="brand-name">Harrowfield Nature Alliance</span>
    </div>

    <div class="photo photo-fish-board" role="img" aria-label="Photo of grilled fish with lemon slices and tomatoes on a wooden board"></div>

    <div class="date-badge">
      <span class="date-day-num">12TH</span>
      <span class="date-month">FEBRUARY</span>
      <span class="date-weekday">SUNDAY</span>
    </div>

    <h1 class="title">
      <div class="title-fish">Fish</div>
      <div class="title-fry">FRY</div>
    </h1>

    <div class="prices">
      <div class="price-row"><span class="price-label">FOR ADULTS</span><span class="price-value">$15</span></div>
      <div class="price-row"><span class="price-label">FOR 12 &amp; UNDER</span><span class="price-value">$10</span></div>
    </div>

    <div class="free-badge">
      <svg viewBox="0 0 270 140" aria-hidden="true">
        <path fill="var(--orange)" d="M8 14 L262 4 L256 40 L268 74 L258 132 L12 138 L2 100 L14 66 Z"/>
      </svg>
      <div class="free-text">
        <span class="free-word">FREE</span>
        <span class="free-sub">FOR PRESCHOOL</span>
      </div>
    </div>

    <div class="photo photo-plate" role="img" aria-label="Photo of fried fish served on a plate with greens"></div>

    <div class="details">
      <div class="detail-label">LOCATION:</div>
      <div class="detail-value">BRENMOOR SPORTSDOME AUDITORIUM</div>
      <div class="detail-label">TIME:</div>
      <div class="detail-value">5-6:30 PM</div>
    </div>

    <div class="stamp"><div class="stamp-inner">FISH<br>FRY</div></div>
  </main>
</body>
</html>
```